Bold Modern Creative Wine Label Needed for a Chardonnay

We need a modern, eye catching label, one that will appeal to millennials, but also attract the older more conservative crowd. We like the boldness of black on white but are open to your suggestions. Since the bottle type is a light green 'burgundy style' bottle, you should take that into account. The name of the brand is Vo`. The attached label is example of what we like very much. It is eye catching and bold and modern. Keep in mind that the bottle will be light green in color so black and white might not work so well. Use your creativity please! The label can be any size but needs to fit on this shape bottle. See attached photos. thanks!!

(Please no grapes or wine glasses or wine bottles featured on the label!)
Updates

Hi Designers, I just wanted to let you know that we received many great designs and we are sorting through them this week. The website is making it a bit difficult to create a 'poll' so this is taking longer than we expected. Thanks for all the great submissions!

```html
<!DOCTYPE html>
<html lang="en">
<head>
<meta charset="utf-8">
<title>Vo` Chardonnay Label</title>
<link rel="stylesheet" href="https://fonts.googleapis.com/css2?family=Bodoni+Moda:wght@500;600&display=swap">
<style>
  :root {
    --backdrop: #ffffff;
    --paper: #f3f2ee;
    --paper-edge: #e4e2dc;
    --ink: #1f1f1f;
    --ink-soft: #5a5a5a;
  }
  * { margin: 0; padding: 0; box-sizing: border-box; }
  html, body {
    width: 1200px;
    height: 1000px;
    overflow: hidden;
    background: var(--backdrop);
  }
  .canvas {
    position: relative;
    width: 1200px;
    height: 1000px;
  }
  .label {
    position: absolute;
    left: 240px;
    top: 100px;
    width: 720px;
    height: 800px;
    background: var(--paper);
    border: 1px solid var(--paper-edge);
  }
  .varietal {
    position: absolute;
    left: 173px;
    top: 368px;
    transform: translate(-50%, -50%) rotate(-90deg);
    font-family: "Bodoni Moda", serif;
    font-weight: 500;
    font-size: 27px;
    letter-spacing: 2px;
    color: var(--ink-soft);
    text-transform: uppercase;
    white-space: nowrap;
  }
  .brand-name {
    position: absolute;
    left: 205px;
    top: 150px;
    font-family: "Bodoni Moda", serif;
    font-weight: 600;
    font-size: 300px;
    line-height: 1;
    color: var(--ink);
    white-space: nowrap;
  }
</style>
</head>
<body>
  <main class="canvas">
    <section class="label">
      <p class="varietal">Chardonnay</p>
      <h1 class="brand-name">Vo`</h1>
    </section>
  </main>
</body>
</html>
```